New business cards for our company KWTR

We need a new business card design for our existing company. We are a consulting/engineering firm which mainly works in the utility business. We would like to see designs which are pretty traditional and simple, with our logo, maybe with an option of a QR code on the back. We plan on using traditional rectangular horizontal format. Want our logo to be in red as attached, then company info in black or blue. I think we want a clean white card, no full color cards. Website is www.kwtr-example.com.

Industry/Entity Type

Business

Contact Information for Business Card

Want a rectangular horizontal business card layout. Probably want a traditional layout with company logo on top right or top left, but open to new ideas. Will want to show company name, address, web address, phone, employee name and title.

Colors
ec1f27
0355a3
ffffff

Requirements
Must have
• business card design,
Nice to have
• QR code on back,
Should not have
• solid back ground card, want white back ground

```html
<!DOCTYPE html>
<html lang="en">
<head>
<meta charset="utf-8">
<title>KWTR Business Cards</title>
<link href="https://fonts.googleapis.com/css2?family=Arimo:wght@400;700&display=swap" rel="stylesheet">
<style>
  :root {
    --brand-red: #ec1f27;
    --brand-blue: #0355a3;
    --card-white: #ffffff;
    --backdrop: #f2f2f2;
    --card-shadow: rgba(0, 0, 0, 0.12);
  }
  * { box-sizing: border-box; margin: 0; padding: 0; }
  html, body {
    width: 1200px;
    height: 873px;
    overflow: hidden;
    background: var(--backdrop);
    font-family: "Arimo", Arial, sans-serif;
  }
  .card-sheet {
    position: relative;
    width: 1200px;
    height: 873px;
    display: flex;
    align-items: center;
    justify-content: center;
    gap: 50px;
  }
  .business-card {
    position: relative;
    width: 525px;
    height: 300px;
    background: var(--card-white);
    box-shadow: 0 6px 24px var(--card-shadow);
  }
  /* Front: contact side */
  .card-front .border-frame {
    position: absolute;
    inset: 16px;
    border: 3px solid var(--brand-red);
  }
  .contact-block {
    position: absolute;
    left: 58px;
    top: 36px;
    right: 40px;
    color: var(--brand-blue);
  }
  .company-names {
    color: var(--brand-red);
    font-weight: 700;
    font-size: 24px;
    line-height: 1.05;
    letter-spacing: 0.2px;
  }
  .employee-name {
    margin-top: 10px;
    font-weight: 700;
    font-size: 19px;
  }
  .employee-title {
    font-size: 15px;
    margin-top: 2px;
  }
  .contact-lines {
    list-style: none;
    margin-top: 8px;
    font-size: 13px;
    line-height: 1.45;
  }
  .contact-lines li {
    display: flex;
    align-items: center;
    gap: 8px;
    white-space: nowrap;
  }
  .contact-icon {
    width: 12px;
    height: 12px;
    flex: none;
  }
  .contact-icon.is-blank { visibility: hidden; }
  .fax-gap { margin-left: 14px; }
  /* Back: brand side */
  .card-back {
    display: flex;
    align-items: center;
    justify-content: center;
  }
  .brand-name {
    color: var(--brand-red);
    font-weight: 700;
    font-size: 96px;
    letter-spacing: 2px;
  }
</style>
</head>
<body>
  <main class="card-sheet">
    <section class="business-card card-front" aria-label="Card front with contact details">
      <div class="border-frame"></div>
      <div class="contact-block">
        <h1 class="company-names">KWTR ENGINEERS<br>KWTR SERVICE CORP</h1>
        <p class="employee-name">Daniel Morrow</p>
        <p class="employee-title">Project Engineer</p>
        <ul class="contact-lines">
          <li>
            <svg class="contact-icon" viewBox="0 0 12 12" aria-hidden="true"><path d="M6 0.5a3.5 3.5 0 0 1 3.5 3.5c0 2.6-3.5 7.5-3.5 7.5S2.5 6.6 2.5 4A3.5 3.5 0 0 1 6 0.5z" fill="var(--brand-blue)"/><circle cx="6" cy="4" r="1.3" fill="var(--card-white)"/></svg>
            418 Ridgeline Rd. Fenton, MO 63026
          </li>
          <li>
            <svg class="contact-icon" viewBox="0 0 12 12" aria-hidden="true"><rect x="0.5" y="2" width="11" height="8" fill="var(--brand-blue)"/><path d="M0.8 2.4 6 6.6l5.2-4.2" stroke="var(--card-white)" stroke-width="1.1" fill="none"/></svg>
            dmorrow@kwtr-example.com
          </li>
          <li>
            <svg class="contact-icon" viewBox="0 0 12 12" aria-hidden="true"><circle cx="6" cy="6" r="5" fill="none" stroke="var(--brand-blue)" stroke-width="1.1"/><path d="M1 6h10M6 1c-2.4 2.8-2.4 7.2 0 10M6 1c2.4 2.8 2.4 7.2 0 10" fill="none" stroke="var(--brand-blue)" stroke-width="0.9"/></svg>
            www.kwtr-example.com
          </li>
          <li>
            <svg class="contact-icon" viewBox="0 0 12 12" aria-hidden="true"><rect x="3" y="0.5" width="6" height="11" rx="1" fill="none" stroke="var(--brand-blue)" stroke-width="1.2"/></svg>
            555.240.1800 <span class="fax-gap">Fax: 555.240.1811</span>
          </li>
          <li>
            <svg class="contact-icon is-blank" viewBox="0 0 12 12" aria-hidden="true"></svg>
            Cell: 555.317.4620
          </li>
        </ul>
      </div>
    </section>
    <section class="business-card card-back" aria-label="Card back with company name">
      <p class="brand-name">KWTR</p>
    </section>
  </main>
</body>
</html>
```